One Page PDF Educational Handout Design for Women and Students

We need a 1-2 page PDF created that outlines 11 steps in a process. The attached style guide contains information on how to design the document (page 1). Pages 2-3 need to be formatted in a visually appealing manner to call attention to the 11 steps and substeps.

We would like the design to include our logo, the title, the steps, and contain colors, sections and stimulating design.

Target Market(s)

College Students, Women 18-30 years old.

Industry/Entity Type

Education

Font styles to use
Sans Serif

Colors
33a6d7
f04a50
f68d4d

Requirements
Must have
• Colors, Logo, Titles, Organized by Title/Subtitle. 1-2 pages. Visually stimulating and appealing.

```html
<!DOCTYPE html>
<html lang="en">
<head>
<meta charset="utf-8">
<title>Nursing Test Taking Tips – Handout</title>
<link href="https://fonts.googleapis.com/css2?family=Montserrat:wght@700;800;900&family=Raleway:wght@400;500;700&family=Roboto+Condensed:wght@700&display=swap" rel="stylesheet">
<style>
  :root{
    --coral:#f06464;
    --blue:#6a9ec9;
    --green:#72b87c;
    --ink:#4a4a4a;
    --dark:#505256;
    --paper:#ffffff;
    --stage:#e6e6e8;
  }
  *{box-sizing:border-box;margin:0;padding:0}
  html,body{width:1200px;height:1200px;overflow:hidden;background:var(--stage)}
  .page{position:absolute;top:202px;width:540px;height:764px;background:var(--paper);overflow:hidden}
  .page--cover{left:54px}
  .page--tips{left:604px}

  /* cover */
  .cover__photo{position:absolute;left:0;top:90px;width:540px;height:560px;
    background:radial-gradient(ellipse at 45% 45%,#e9d8cc 0%,#d7c2b4 22%,#eef1f5 48%,#ffffff 75%)}
  .brand{position:absolute;top:40px;right:32px;display:flex;align-items:center;gap:14px}
  .brand__mark{width:44px;height:44px;background:var(--blue);border-radius:3px}
  .brand__name{font-family:"Montserrat",sans-serif;font-weight:800;font-size:38px;color:var(--dark);letter-spacing:-1px}
  .cover__waves{position:absolute;left:0;top:0}
  .badge{position:absolute;left:322px;top:476px;width:172px;height:172px;border-radius:50%;
    background:var(--paper);display:flex;align-items:center;justify-content:center}
  .badge__inner{width:148px;height:148px;border-radius:50%;background:var(--coral);display:flex;align-items:center;justify-content:center;
    font-family:"Montserrat",sans-serif;font-weight:900;font-size:112px;color:#fff;letter-spacing:-8px;padding-right:8px}
  .cover__title{position:absolute;right:32px;top:664px;text-align:right;font-family:"Montserrat",sans-serif;font-weight:900;
    font-size:43px;line-height:44px;color:#fff;letter-spacing:-0.5px}

  /* tips */
  .tip{position:absolute;width:250px}
  .tip__num{position:absolute;left:0;top:0;width:43px;height:42px;background:var(--coral);color:#fff;
    font-family:"Roboto Condensed",sans-serif;font-weight:700;font-size:38px;line-height:44px;text-align:center;letter-spacing:-1px}
  .tip__body{margin-left:57px}
  .tip__title{font-family:"Raleway",sans-serif;font-weight:700;font-size:14.5px;line-height:15.5px;color:var(--coral);text-transform:uppercase;margin-bottom:3px;margin-top:6px}
  .tip__list{list-style:none;font-family:"Raleway",sans-serif;font-size:11px;line-height:13px;color:var(--ink)}
  .tip__list>li{position:relative;padding-left:10px;margin-bottom:4px}
  .tip__list>li::before{content:"·";position:absolute;left:0;top:0;font-weight:700}
  .tip__sub{list-style:none;margin-top:3px;padding-left:11px;font-size:8.6px;line-height:10.6px}
  .tip__sub li{position:relative;padding-left:0;margin-bottom:3px}
  .tip__sub li::before{content:"·";position:absolute;left:-9px;font-weight:700}
  .tip__sub b{font-weight:700;color:#333}

  .tips__footer{position:absolute;left:0;top:620px}
  .tips__note{position:absolute;left:22px;top:697px;font-family:"Raleway",sans-serif;font-size:11px;line-height:13px;color:#fff}
  .tips__note small{font-size:8.5px}
  .tips__visit{position:absolute;right:22px;top:726px;font-family:"Raleway",sans-serif;font-size:18px;color:#fff}
  .tips__visit b{font-weight:700}
</style>
</head>
<body>

<section class="page page--cover">
  <div class="cover__photo" role="img" aria-label="Photo of a smiling nurse in a white coat with a stethoscope holding a clipboard"></div>
  <div class="brand">
    <span class="brand__mark"></span>
    <span class="brand__name">CAREWAVE</span>
  </div>
  <svg class="cover__waves" width="540" height="764" viewBox="0 0 540 764">
    <path d="M0 610 C160 585 340 560 540 540 L540 764 L0 764 Z" fill="var(--coral)"/>
    <path d="M0 645 C170 630 330 600 430 570 C480 556 515 572 540 580 L540 764 L0 764 Z" fill="var(--blue)"/>
  </svg>
  <div class="badge"><div class="badge__inner">11</div></div>
  <h1 class="cover__title">NURSING TEST<br>TAKING TIPS</h1>
</section>

<section class="page page--tips">
  <article class="tip" style="left:21px;top:26px">
    <div class="tip__num">01</div>
    <div class="tip__body"><h2 class="tip__title">SATA</h2>
      <ul class="tip__list"><li>Evaluate each option individuals</li><li>Rearrange as a True/False Question</li></ul></div>
  </article>
  <article class="tip" style="left:21px;top:111px">
    <div class="tip__num">02</div>
    <div class="tip__body"><h2 class="tip__title">Absolute Words</h2>
      <ul class="tip__list"><li>Always, Never, None, All, Every</li><li>RED FLAGS</li><li>May be correct if it's a safety issue</li></ul></div>
  </article>
  <article class="tip" style="left:21px;top:203px">
    <div class="tip__num">03</div>
    <div class="tip__body"><h2 class="tip__title">Opposites</h2>
      <ul class="tip__list"><li>Two opposite answer choices usually means one is correct</li><li>Review before other options</li><li>Hyper vs Hypo, Acute vs Chronic, Overload vs Deficit</li></ul></div>
  </article>
  <article class="tip" style="left:21px;top:322px">
    <div class="tip__num">04</div>
    <div class="tip__body"><h2 class="tip__title">Opposites</h2>
      <ul class="tip__list"><li>Answer options with the same concept means both are usually incorrect</li></ul></div>
  </article>
  <article class="tip" style="left:21px;top:404px">
    <div class="tip__num">05</div>
    <div class="tip__body"><h2 class="tip__title">Priority</h2>
      <ul class="tip__list"><li>ABCs, Pain, Education, Feelings</li><li>Which option is closest to Airway</li>
        <li>ABCs
          <ul class="tip__sub">
            <li><b>Airway:</b> NPO, gag reflex, breathing, airway</li>
            <li><b>Breathing:</b> breath sounds, O2 admin, pulse ox, raise HOB</li>
            <li><b>Circulation:</b> HR, BP, CPR, fluid status, diarrhea, IV fluids, central lines, bleeding</li>
            <li><b>Safety:</b> physical (rugs, nightlight, phone, falls) infection (assessing, temp, hand washing, cultures, antibiotics, wounds)</li>
          </ul></li>
        <li>Keywords: priority, emergency, ambulance, returning to floor, see first</li></ul></div>
  </article>

  <article class="tip" style="left:281px;top:25px">
    <div class="tip__num">06</div>
    <div class="tip__body"><h2 class="tip__title">Nursing Process</h2>
      <ul class="tip__list"><li>Always follow ADPIE</li></ul></div>
  </article>
  <article class="tip" style="left:281px;top:91px">
    <div class="tip__num">07</div>
    <div class="tip__body"><h2 class="tip__title">Acute vs Chronic</h2>
      <ul class="tip__list"><li>Content is KING</li><li>If the question is asking about ACUTE condition, one of the options will be about CHRONIC</li><li>Acute vs Chronic, Short Term vs Long Term, Early Signs vs Late Signs</li></ul></div>
  </article>
  <article class="tip" style="left:281px;top:228px">
    <div class="tip__num">08</div>
    <div class="tip__body"><h2 class="tip__title">What do they<br>want to know?</h2>
      <ul class="tip__list"><li>Read every word of the question</li><li>Remove distractors</li><li>Don't overthink</li><li>Correct or Incorrect Answer (except/further teaching)</li></ul></div>
  </article>
  <article class="tip" style="left:281px;top:354px">
    <div class="tip__num">09</div>
    <div class="tip__body"><h2 class="tip__title">Expected findings vs complications</h2>
      <ul class="tip__list"><li>Rule out expected findings</li></ul></div>
  </article>
  <article class="tip" style="left:281px;top:424px">
    <div class="tip__num">10</div>
    <div class="tip__body"><h2 class="tip__title">Repeating Words</h2>
      <ul class="tip__list"><li>Last ditch effort, when all else fails</li><li>Look for repeating words in question and answer options</li></ul></div>
  </article>
  <article class="tip" style="left:281px;top:506px">
    <div class="tip__num">11</div>
    <div class="tip__body"><h2 class="tip__title">Board Exam<br>Question Traps</h2>
      <ul class="tip__list"><li>No Assessment</li><li>Incomplete Assessment</li><li>Incorrect Assessment</li><li>“First” doesn't always mean assessment</li><li>“Action” doesn't always mean implementation</li><li>Determine the outcome of each answer option</li></ul></div>
  </article>

  <svg class="tips__footer" width="540" height="144" viewBox="0 0 540 144">
    <path d="M0 30 C110 10 200 30 290 58 C380 84 470 74 540 48 L540 144 L0 144 Z" fill="var(--blue)"/>
    <path d="M0 40 C110 25 200 40 290 66 C380 92 470 86 540 62 L540 144 L0 144 Z" fill="var(--green)"/>
  </svg>
  <p class="tips__note">Use this guide to work through tests.<br>Remember CONTENT is king.&nbsp; Learn all you can.<br>Save $75 on Carewave Academy while available.<br><small>©2017 carewave.com</small></p>
  <p class="tips__visit">Visit <b>carewave.com/study</b></p>
</section>

</body>
</html>
```